Morrow Poolworks, LLC Business Card

We have a well designed logo that we need incorporated into a professional and unique business card. Morrow Poolworks provides professional swimming pool management. From openings to closings, inspections, chemicals, maintenance, lifeguard, safety audits, learn to swim lessons, etc. etc.
Different colors of blue are ideal. The final design should include water, clean water (very clean crystal clear water), and perhaps safety.
content/design ideas:
Felix Brant, President - Owner
felix@morrowpoolworks.example
office: 555-410-3826
cell: 555-962-1507
www.morrowpoolworks.example
"Your Pool: Safer, Cleaner, Clearer"
Target Market(s)
Our customers are mostly home owners associations and property management companies. Adults, aged 25 to 55. Mostly with young children.
Industry/Entity Type
Safety
Look and feel

```html
<!DOCTYPE html>
<html lang="en">
<head>
<meta charset="utf-8">
<title>Morrow Poolworks, LLC Business Card</title>
<link rel="stylesheet" href="https://fonts.googleapis.com/css2?family=Source+Sans+3:ital,wght@0,400;0,600;0,700;1,400&display=swap">
<style>
  :root {
    --page: #ececec;
    --card: #ffffff;
    --card-edge: #c9c9c9;
    --brand-blue: #1f86c8;
    --band-blue: #2a95d4;
    --deep-blue: #1565a8;
    --water-light: #5fd0f5;
    --water-mid: #1fb0ea;
    --water-deep: #0f8fd6;
    --white: #ffffff;
  }
  * { margin: 0; padding: 0; box-sizing: border-box; }
  html, body { width: 1200px; height: 1200px; overflow: hidden; }
  body {
    background: var(--page);
    font-family: "Source Sans 3", "Myriad Pro", Arial, sans-serif;
    position: relative;
  }
  .card {
    position: absolute;
    left: 206px;
    width: 838px;
    height: 476px;
    border-radius: 36px;
    overflow: hidden;
  }
  .card-front {
    top: 90px;
    background: var(--card);
    border: 1px solid var(--card-edge);
  }
  .card-back { top: 614px; }

  /* front */
  .brand {
    position: absolute;
    left: 62px;
    top: 160px;
    display: flex;
    align-items: center;
    gap: 14px;
    color: var(--deep-blue);
    font-weight: 600;
    font-size: 44px;
    line-height: 1;
    white-space: nowrap;
  }
  .brand-dot {
    width: 26px; height: 26px; border-radius: 50%;
    background: var(--deep-blue);
  }
  .brand-suffix { font-size: 18px; align-self: flex-end; margin-left: -8px; }
  .name-band {
    position: absolute;
    left: 278px;
    top: 263px;
    width: 560px;
    height: 39px;
    background: var(--band-blue);
    color: var(--white);
    display: flex;
    align-items: center;
    padding-left: 90px;
    font-size: 26px;
    white-space: nowrap;
  }
  .person-name { font-weight: 600; }
  .divider { width: 1px; height: 26px; background: var(--white); margin: 0 10px; }
  .person-title { font-style: italic; font-weight: 400; }
  .contact-list {
    position: absolute;
    left: 368px;
    top: 322px;
    list-style: none;
  }
  .contact-item {
    display: flex;
    align-items: center;
    gap: 12px;
    height: 41px;
    color: var(--brand-blue);
    font-weight: 600;
    font-size: 23px;
  }
  .contact-icon {
    width: 32px; height: 32px; border-radius: 50%;
    background: var(--brand-blue);
    display: flex; align-items: center; justify-content: center;
  }

  /* back */
  .pool-photo {
    position: absolute; inset: 0;
    background:
      radial-gradient(ellipse 45% 55% at 15% 70%, #dfe6ea 0%, #c9d3d8 60%, rgba(201,211,216,0) 62%),
      linear-gradient(160deg, var(--water-light) 0%, var(--water-mid) 50%, var(--water-deep) 100%);
  }
  .back-brand {
    position: absolute;
    right: 40px;
    top: 92px;
    display: flex;
    align-items: center;
    gap: 10px;
    color: var(--white);
    font-weight: 600;
    font-size: 29px;
    white-space: nowrap;
  }
  .back-brand .brand-dot { width: 18px; height: 18px; background: var(--white); }
  .back-brand .brand-suffix { font-size: 13px; margin-left: -6px; }
  .tagline {
    position: absolute;
    right: 38px;
    top: 278px;
    text-align: right;
    color: var(--white);
    font-weight: 600;
    font-size: 24px;
    letter-spacing: 2px;
    line-height: 27px;
  }
  .tagline-lead { margin-bottom: 6px; }
  .tagline-item::after { content: " \25C2"; font-size: 14px; }
  .web-address {
    position: absolute;
    right: 38px;
    top: 424px;
    color: var(--white);
    font-weight: 600;
    font-size: 23px;
    letter-spacing: 2px;
  }
</style>
</head>
<body>
  <section class="card card-front">
    <div class="brand">
      <span class="brand-dot"></span>
      <span>Morrow Poolworks</span><span class="brand-suffix">LLC</span>
    </div>
    <div class="name-band">
      <span class="person-name">Felix Brant</span>
      <span class="divider"></span>
      <span class="person-title">President - Owner</span>
    </div>
    <ul class="contact-list">
      <li class="contact-item">
        <span class="contact-icon">
          <svg width="20" height="14" viewBox="0 0 20 14"><rect x="1" y="1" width="18" height="12" fill="none" stroke="#fff" stroke-width="1.6"/><path d="M1 1 L10 8 L19 1" fill="none" stroke="#fff" stroke-width="1.6"/></svg>
        </span>
        felix@morrowpoolworks.example
      </li>
      <li class="contact-item">
        <span class="contact-icon">
          <svg width="12" height="20" viewBox="0 0 12 20"><rect x="1" y="1" width="10" height="18" rx="2" fill="none" stroke="#fff" stroke-width="1.6"/><rect x="3" y="3.5" width="6" height="5" fill="#fff"/><circle cx="4" cy="12" r="0.9" fill="#fff"/><circle cx="8" cy="12" r="0.9" fill="#fff"/><circle cx="4" cy="15" r="0.9" fill="#fff"/><circle cx="8" cy="15" r="0.9" fill="#fff"/></svg>
        </span>
        555-962-1507
      </li>
      <li class="contact-item">
        <span class="contact-icon">
          <svg width="18" height="18" viewBox="0 0 24 24"><path fill="#fff" d="M6.6 10.8a15.1 15.1 0 0 0 6.6 6.6l2.2-2.2c.3-.3.7-.4 1-.2 1.1.4 2.3.6 3.6.6.6 0 1 .4 1 1V20c0 .6-.4 1-1 1C10.6 21 3 13.4 3 4c0-.6.4-1 1-1h3.5c.6 0 1 .4 1 1 0 1.3.2 2.5.6 3.6.1.3 0 .7-.2 1z"/></svg>
        </span>
        555-410-3826
      </li>
    </ul>
  </section>

  <section class="card card-back">
    <div class="pool-photo" role="img" aria-label="Photograph of crystal clear blue pool water with a curved tiled deck, pool ladder and patio table with chairs"></div>
    <div class="back-brand">
      <span class="brand-dot"></span>
      <span>Morrow Poolworks</span><span class="brand-suffix">LLC</span>
    </div>
    <div class="tagline">
      <div class="tagline-lead">Your Pool</div>
      <div class="tagline-item">Safer</div>
      <div class="tagline-item">Cleaner</div>
      <div class="tagline-item">Clearer</div>
    </div>
    <div class="web-address">www.morrowpoolworks.example</div>
  </section>
</body>
</html>
```